wealth management firm, professional group, new model

we have a logo that works but we need a card, white background using our colors...clean look

our tag line if can be used in

The Bridge From Client to Owner

```html
<!DOCTYPE html>
<html lang="en">
<head>
<meta charset="utf-8">
<title>Ovreth Wealth Partners — Business Card</title>
<link href="https://fonts.googleapis.com/css2?family=Poppins:wght@300;400;600;700&display=swap" rel="stylesheet">
<style>
  :root {
    --backdrop: #bdbec0;
    --card: #ffffff;
    --navy: #14223f;
    --ink: #1e2d4d;
    --muted: #7a7a7a;
    --rule: #a9a9a9;
  }
  * { box-sizing: border-box; margin: 0; padding: 0; }
  html, body {
    width: 1200px; height: 1000px; overflow: hidden;
    background: var(--backdrop);
    font-family: "Poppins", sans-serif;
  }
  .canvas { position: relative; width: 1200px; height: 1000px; }
  .card {
    position: absolute; left: 281px; width: 639px; height: 357px;
    background: var(--card); border-radius: 20px;
  }
  .card--front { top: 110px; }
  .card--back { top: 536px; }

  .brand { color: var(--navy); font-weight: 400; line-height: 1; white-space: nowrap; }
  .card--front .brand {
    position: absolute; left: 0; right: 0; top: 170px; text-align: center;
  }
  .card--front .brand__name {
    display: block; font-size: 58px; letter-spacing: 0.34em; padding-left: 0.34em;
  }
  .card--front .brand__sub {
    display: block; margin-top: 28px; font-size: 22px; letter-spacing: 0.12em;
  }
  .card--back .brand {
    position: absolute; left: 30px; top: 85px; width: 180px; text-align: center;
  }
  .card--back .brand__name {
    display: block; font-size: 24px; letter-spacing: 0.34em; padding-left: 0.34em;
  }
  .card--back .brand__sub {
    display: block; margin-top: 12px; font-size: 11px; letter-spacing: 0.1em;
  }

  .person { position: absolute; left: 38px; top: 210px; color: var(--ink); }
  .person__name { font-size: 23px; font-weight: 600; line-height: 1.15; }
  .person__title { font-size: 15px; letter-spacing: 0.18em; margin-top: 0; font-weight: 400; line-height: 1.3; }

  .rule {
    position: absolute; left: 29px; right: 29px; top: 267px;
    border-top: 1px solid var(--rule);
  }
  .contact {
    position: absolute; left: 40px; top: 279px; list-style: none;
    color: var(--muted); font-size: 18px; font-weight: 300; line-height: 21px;
  }
  .contact li { display: flex; align-items: center; gap: 9px; }
  .contact svg { width: 18px; height: 15px; fill: var(--navy); }
  .website {
    position: absolute; right: 28px; top: 300px;
    font-size: 18px; line-height: 22px; color: var(--muted);
  }
  .website strong { color: var(--ink); font-weight: 700; }
</style>
</head>
<body>
<main class="canvas">
  <section class="card card--front">
    <div class="brand">
      <span class="brand__name">OVRETH</span>
      <span class="brand__sub">WEALTH PARTNERS</span>
    </div>
  </section>

  <section class="card card--back">
    <div class="brand">
      <span class="brand__name">OVRETH</span>
      <span class="brand__sub">WEALTH PARTNERS</span>
    </div>

    <div class="person">
      <p class="person__name">Name Surname</p>
      <p class="person__title">TITLE</p>
    </div>

    <div class="rule"></div>

    <ul class="contact">
      <li>
        <svg viewBox="0 0 24 24" aria-hidden="true"><path d="M6.6 10.8c1.4 2.8 3.8 5.1 6.6 6.6l2.2-2.2c.3-.3.7-.4 1-.2 1.1.4 2.3.6 3.6.6.6 0 1 .4 1 1V20c0 .6-.4 1-1 1C10.6 21 3 13.4 3 4c0-.6.4-1 1-1h3.5c.6 0 1 .4 1 1 0 1.3.2 2.5.6 3.6.1.3 0 .7-.2 1l-2.3 2.2z"/></svg>
        <span>012 345 6789</span>
      </li>
      <li>
        <svg viewBox="0 0 24 18" aria-hidden="true"><path d="M0 1l12 9L24 1V0H0zM0 3.5V18h24V3.5l-12 9z"/></svg>
        <span>email@ovrethwealth.com</span>
      </li>
    </ul>

    <p class="website"><strong>ovrethwealth</strong>.com</p>
  </section>
</main>
</body>
</html>
```